BRIM Outreach Partners Business Card Rebrand

Hello Designers! We are looking for help designing our new business card to go in conjunction with our company rebrand. Unfortunately, we have an event mid June that requires we get these printed ASAP (before our new website is launched.) We have a mostly complete Brand Book which I have uploaded to this request for your reference to company information, style, fonts. I've also enclosed our logo file in .eps & .jpg. Attached is a sample business card my boss liked but said was "too simple." I made it in Canva and do not profess to be a designer. NOT FOR DESIGN REFERENCE, ONLY FOR CONTEXT Here is what our old website looks like: https://brimoutreachpartners.com/.

```html
<!DOCTYPE html>
<html lang="en">
<head>
<meta charset="utf-8">
<title>BRIM Outreach Partners – Business Card</title>
<link rel="stylesheet" href="https://fonts.googleapis.com/css2?family=Arimo:wght@400;700&display=swap">
<style>
  :root {
    --bg: #e9ebee;
    --card-white: #ffffff;
    --brand-blue: #43b0e5;
    --brand-blue-deep: #2f9bd2;
    --ink: #141414;
    --grey: #6b6b6b;
  }
  * { margin: 0; padding: 0; box-sizing: border-box; }
  html, body { width: 1200px; height: 1108px; overflow: hidden; }
  body {
    background: var(--bg);
    font-family: "Arimo", Arial, sans-serif;
    position: relative;
  }
  .card {
    position: absolute;
    top: 186px;
    width: 420px;
    height: 735px;
    border-radius: 30px;
    overflow: hidden;
    box-shadow: 0 10px 30px rgba(0,0,0,0.12);
  }
  .card--front { left: 150px; background: var(--card-white); }
  .card--back { left: 630px; background: var(--brand-blue); }

  .brand {
    display: flex;
    align-items: center;
    justify-content: center;
    gap: 14px;
  }
  .brand__dot {
    width: 62px; height: 62px;
    border-radius: 50%;
    flex: none;
  }
  .brand__name {
    font-weight: 700;
    font-size: 27px;
    line-height: 1.05;
    letter-spacing: -0.3px;
  }
  .card--front .brand { margin-top: 120px; }
  .card--front .brand__dot { background: var(--brand-blue); }
  .card--front .brand__name { color: var(--ink); }

  .person { text-align: center; margin-top: 64px; }
  .person__name { font-size: 28px; font-weight: 700; color: var(--ink); }
  .person__name .surname { color: var(--brand-blue); }
  .person__role { font-size: 19px; color: var(--grey); margin-top: 6px; }

  .icon-rule {
    display: flex; align-items: center; gap: 8px;
    margin: 26px 50px 0;
  }
  .icon-rule__line { flex: 1; height: 1.5px; background: var(--brand-blue); }
  .icon-tile {
    width: 28px; height: 28px; border-radius: 5px;
    background: var(--brand-blue);
    display: flex; align-items: center; justify-content: center;
  }
  .contact {
    text-align: center; margin-top: 22px;
    font-size: 20px; line-height: 1.3; color: var(--ink);
  }
  .contact .web-name { color: var(--brand-blue); }
  .divider { height: 1.5px; background: var(--brand-blue); margin: 26px 50px 0; }
  .location {
    text-align: center; margin-top: 24px;
    font-size: 19px; line-height: 1.35; color: var(--grey);
  }

  .card--back .brand { height: 100%; }
  .card--back .brand__dot { background: var(--card-white); }
  .card--back .brand__name { color: var(--card-white); }
  .back-texture {
    position: absolute; inset: 0;
    background: linear-gradient(160deg, var(--brand-blue) 0%, var(--brand-blue) 55%, var(--brand-blue-deep) 100%);
  }
  .card--back .brand { position: relative; }
</style>
</head>
<body>
  <section class="card card--front" aria-label="Business card front">
    <div class="brand">
      <span class="brand__dot"></span>
      <span class="brand__name">BRIM Outreach<br>Partners</span>
    </div>

    <div class="person">
      <p class="person__name">Daniel <span class="surname">Marsh-Holloway</span></p>
      <p class="person__role">Managing Partner</p>
    </div>

    <div class="icon-rule">
      <span class="icon-rule__line"></span>
      <span class="icon-tile">
        <svg width="18" height="18" viewBox="0 0 24 24" aria-label="Phone"><path fill="#fff" d="M6.6 10.8a15 15 0 0 0 6.6 6.6l2.2-2.2a1 1 0 0 1 1-.25 11.4 11.4 0 0 0 3.6.57 1 1 0 0 1 1 1V20a1 1 0 0 1-1 1A17 17 0 0 1 3 4a1 1 0 0 1 1-1h3.5a1 1 0 0 1 1 1c0 1.25.2 2.45.57 3.57a1 1 0 0 1-.25 1z"/></svg>
      </span>
      <span class="icon-tile">
        <svg width="18" height="18" viewBox="0 0 24 24" aria-label="Email"><rect x="3" y="6" width="18" height="12" rx="1.5" fill="#fff"/><path d="M3.5 6.5 12 13l8.5-6.5" fill="none" stroke="#43b0e5" stroke-width="1.6"/></svg>
      </span>
      <span class="icon-tile">
        <svg width="18" height="18" viewBox="0 0 24 24" aria-label="Website"><g fill="none" stroke="#fff" stroke-width="1.8"><circle cx="12" cy="12" r="8.5"/><ellipse cx="12" cy="12" rx="3.8" ry="8.5"/><path d="M3.5 12h17"/></g></svg>
      </span>
      <span class="icon-rule__line"></span>
    </div>

    <div class="contact">
      <p>+945-555-0142</p>
      <p>daniel@brimoutreachpartners.com</p>
      <p>www.<span class="web-name">brimoutreachpartners</span>.com</p>
    </div>

    <div class="divider"></div>

    <div class="location">
      <p>Atlanta</p>
      <p>GA based (Central Time)</p>
    </div>
  </section>

  <section class="card card--back" aria-label="Business card back">
    <div class="back-texture" role="img" aria-label="Embossed repeating brand pattern in tones of blue"></div>
    <div class="brand">
      <span class="brand__dot"></span>
      <span class="brand__name">BRIM Outreach<br>Partners</span>
    </div>
  </section>
</body>
</html>
```